Harborline Crest Insurance Services

we are a high end insurance agency we specialize on Auto | Home | Business | Life looking for something professional and luxuries at the same time. if you guys need anything else please let me know.

Auto | Home | Business | Life must be under logo on the back with black background.

i want the back part to be black with our gold logo on it.

Target Market(s)

Auto | Home | Business | Life

Industry/Entity Type

Insurance Broker

Contact Information for Business Card

My logo is gold so a black in the back would be nice.

Font styles to use
Serif

Colors
000000

Requirements
Must have
• Big logo on the back with black background.

```html
<!DOCTYPE html>
<html lang="en">
<head>
<meta charset="utf-8">
<title>Harborline Crest Insurance Services – Business Card</title>
<link href="https://fonts.googleapis.com/css2?family=Arimo:wght@400&family=Libre+Baskerville:wght@400;700&family=Montserrat:wght@400;500&display=swap" rel="stylesheet">
<style>
  :root {
    --page: #ffffff;
    --card: #000000;
    --card-edge: #1a1a1a;
    --gold: #f2b816;
    --silver: #c9c9cb;
    --grey-text: #a9a9ab;
    --rule: #8e8e90;
    --label: #333333;
  }
  * { margin: 0; padding: 0; box-sizing: border-box; }
  html, body {
    width: 1200px; height: 528px; overflow: hidden;
    background: var(--page);
  }
  .sheet { position: relative; width: 1200px; height: 528px; }

  .side-label {
    position: absolute; top: 62px; width: 536px;
    text-align: center;
    font: 400 48px/1 "Arimo", Arial, sans-serif;
    color: var(--label);
  }
  .side-label--front { left: 29px; }
  .side-label--back { left: 611px; }

  .card {
    position: absolute; top: 134px;
    width: 536px; height: 328px;
    border-radius: 24px;
    background: linear-gradient(180deg, #0b0b0b 0%, var(--card) 55%, #050505 100%);
    box-shadow: 0 0 0 1px var(--card-edge);
    overflow: hidden;
  }
  .card--front { left: 29px; }
  .card--back { left: 611px; }

  .card__rule {
    position: absolute; left: 0; right: 0; top: 239px; height: 3px;
    background: linear-gradient(90deg, #d8d8d8 0%, var(--rule) 12%, var(--rule) 100%);
  }
  .card__services {
    position: absolute; left: 0; right: 0; top: 265px;
    text-align: center;
    font: 500 18px/1 "Montserrat", Arial, sans-serif;
    letter-spacing: 4.2px;
    color: var(--silver);
  }

  /* Front */
  .brand-mini {
    position: absolute; left: 44px; top: 38px;
    display: flex; align-items: center; gap: 8px;
  }
  .brand-mini__dot {
    width: 30px; height: 30px; border-radius: 50%;
    background: var(--gold);
  }
  .brand-mini__name {
    font: 700 11px/1.25 "Libre Baskerville", Georgia, serif;
    color: var(--gold);
    letter-spacing: 0.3px;
  }
  .holder-name {
    position: absolute; left: 0; right: 0; top: 104px;
    text-align: center;
    font: 700 50px/1 "Libre Baskerville", Georgia, serif;
    color: var(--gold);
    letter-spacing: -0.5px;
  }
  .holder-title {
    position: absolute; left: 0; right: 0; top: 165px;
    text-align: center; padding-left: 8px;
    font: 400 19px/1 "Montserrat", Arial, sans-serif;
    letter-spacing: 6px;
    color: var(--silver);
  }
  .contact {
    position: absolute; top: 215px;
    font: 400 17px/1 "Arimo", Arial, sans-serif;
    color: var(--grey-text);
  }
  .contact--email { left: 44px; }
  .contact--phone { right: 42px; }

  /* Back */
  .brand-mark {
    position: absolute; left: 50%; top: 36px;
    width: 96px; height: 96px; margin-left: -48px;
    border-radius: 50%;
    background: var(--gold);
  }
  .brand-name {
    position: absolute; left: 0; right: 0; top: 160px;
    text-align: center;
    font: 700 22px/1.3 "Libre Baskerville", Georgia, serif;
    color: var(--gold);
  }
  .brand-name__line { display: block; }
  .brand-name__line--sub { font-size: 12px; letter-spacing: 4px; }
</style>
</head>
<body>
<main class="sheet">
  <h2 class="side-label side-label--front">Front</h2>
  <h2 class="side-label side-label--back">Back</h2>

  <section class="card card--front" aria-label="Business card front">
    <div class="brand-mini">
      <span class="brand-mini__dot"></span>
      <span class="brand-mini__name">Harborline Crest<br>Insurance Services</span>
    </div>
    <h1 class="holder-name">Your Name</h1>
    <p class="holder-title">PRESIDENT</p>
    <p class="contact contact--email">email@yoursite.com</p>
    <p class="contact contact--phone">123 456 7890</p>
    <div class="card__rule"></div>
    <p class="card__services">AUTO | HOME | BUSINESS | LIFE</p>
  </section>

  <section class="card card--back" aria-label="Business card back">
    <span class="brand-mark"></span>
    <p class="brand-name">
      <span class="brand-name__line">Harborline Crest</span>
      <span class="brand-name__line brand-name__line--sub">INSURANCE SERVICES</span>
    </p>
    <div class="card__rule"></div>
    <p class="card__services">AUTO | HOME | BUSINESS | LIFE</p>
  </section>
</main>
</body>
</html>
```